Communication and Marketing agency needs a new presentation card

We are a group of communication and marketing agencies specialized in companies that are in the logistics and industrial sector. The head agency is TELVANO Grupo and the group consists of 4 agencies: TELVANO Media, TELVANO Digital, TELVANO Research and EnlazaPorImagen. We hace 4 offices in Spain (Madrid, Barcelona, Valencia and Murcia). We are looking for a clean and attractive design that transmits our experience, brand presence in the market and knowledge to those who receive the card.It has to maintain the colors of the logo that is attached.
Target Market(s)
logistics and industrial sector
Marketing department
Clean and attractive design

```html
<!DOCTYPE html>
<html lang="es">
<head>
<meta charset="utf-8">
<title>TELVANO Grupo – Tarjeta de presentación</title>
<link href="https://fonts.googleapis.com/css2?family=Montserrat:wght@400;500;600;700&display=swap" rel="stylesheet">
<style>
  :root {
    --bg: #c9c9c9;
    --card-dark: #2c2a29;
    --card-light: #ffffff;
    --brand-red: #b3162b;
    --ink: #2a2a2a;
    --muted: #8a8a8a;
    --map-tone: #5a5756;
  }
  * { box-sizing: border-box; margin: 0; padding: 0; }
  html, body { width: 1200px; height: 930px; overflow: hidden; }
  body {
    background: var(--bg);
    font-family: "Montserrat", sans-serif;
    position: relative;
  }
  .card {
    position: absolute;
    left: 330px;
    width: 540px;
    height: 340px;
    border-radius: 22px;
    overflow: hidden;
    box-shadow: 0 8px 22px rgba(0,0,0,.18);
  }

  /* Back side */
  .card--back { top: 70px; background: var(--card-dark); color: #fff; }
  .office-map {
    position: absolute; left: 150px; top: 30px; width: 240px; height: 160px;
    background: radial-gradient(ellipse at 45% 50%, var(--map-tone), var(--card-dark) 75%);
    border-radius: 14px;
  }
  .office-map svg { position: absolute; inset: 0; }
  .cities {
    position: absolute; top: 206px; width: 100%; text-align: center;
    font-weight: 600; font-size: 15px; letter-spacing: .3px;
  }
  .agencies {
    position: absolute; left: 0; right: 0; top: 258px;
    display: flex; justify-content: center; gap: 22px; flex-wrap: wrap; padding: 0 24px;
  }
  .agency { font-size: 14px; font-weight: 500; color: var(--muted); letter-spacing: .5px; }
  .agency--accent { color: var(--brand-red); font-weight: 600; }

  /* Front side */
  .card--front { top: 490px; background: var(--card-light); color: var(--ink); }
  .brand {
    position: absolute; left: 38px; top: 62px;
    font-size: 30px; font-weight: 600; color: var(--brand-red); letter-spacing: 1px;
  }
  .holder { position: absolute; right: 36px; top: 50px; text-align: right; }
  .holder__name { font-size: 20px; font-weight: 600; color: var(--brand-red); }
  .holder__role { font-size: 12px; font-weight: 500; margin-top: 2px; }
  .divider { position: absolute; top: 126px; height: 1px; }
  .divider--grey { left: 38px; width: 230px; background: var(--ink); }
  .divider--red { left: 268px; right: 36px; background: var(--brand-red); }
  .contact {
    position: absolute; left: 38px; top: 196px; list-style: none;
    font-size: 13.5px; font-weight: 500; line-height: 22px;
  }
  .contact li { display: flex; align-items: center; gap: 10px; }
  .contact svg { width: 11px; height: 11px; flex: none; }
  .wave { position: absolute; left: 0; bottom: 0; width: 540px; height: 200px; }
</style>
</head>
<body>

<section class="card card--back" aria-label="Reverso de la tarjeta">
  <div class="office-map" role="img" aria-label="Mapa punteado de España con marcadores en Madrid, Barcelona, Valencia y Murcia">
    <svg viewBox="0 0 240 160" aria-hidden="true">
      <g fill="var(--brand-red)">
        <circle cx="105" cy="70" r="6"/>
        <circle cx="196" cy="36" r="6"/>
        <circle cx="170" cy="82" r="6"/>
        <circle cx="160" cy="118" r="6"/>
      </g>
    </svg>
  </div>
  <p class="cities">Madrid | Barcelona | Valencia | Murcia</p>
  <div class="agencies">
    <span class="agency">TELVANO Digital</span>
    <span class="agency agency--accent">EnlazaPorImagen</span>
    <span class="agency">TELVANO Media</span>
    <span class="agency">TELVANO Research</span>
  </div>
</section>

<section class="card card--front" aria-label="Anverso de la tarjeta">
  <p class="brand">TELVANO Grupo</p>
  <div class="holder">
    <p class="holder__name">Lucía Ferrandis</p>
    <p class="holder__role">Director</p>
  </div>
  <span class="divider divider--grey"></span>
  <span class="divider divider--red"></span>

  <svg class="wave" viewBox="0 0 540 200" preserveAspectRatio="none" aria-hidden="true">
    <path d="M0 200 L0 175 C140 190 250 150 330 80 C400 25 470 20 540 16 L540 200 Z" fill="var(--card-dark)"/>
    <path d="M0 178 C140 192 250 152 330 84 C400 30 470 24 540 20 L540 28 C470 32 405 40 336 94 C255 160 140 196 0 184 Z" fill="var(--brand-red)"/>
    <path d="M0 186 C140 198 258 164 340 100 C410 46 475 38 540 34 L540 40 C478 44 414 54 346 108 C262 172 140 204 0 192 Z" fill="var(--card-light)"/>
  </svg>

  <ul class="contact">
    <li><svg viewBox="0 0 12 12"><path d="M3 1 L5 3.5 L4 5 C5 7 6 8 7 8.5 L8.5 7.5 L11 9.5 L10 11 C5 11 1 6.5 1 2 Z" fill="var(--brand-red)"/></svg>910 555 274</li>
    <li><svg viewBox="0 0 12 12"><rect x="3" y="1" width="6" height="10" rx="1" fill="none" stroke="var(--brand-red)" stroke-width="1.4"/></svg>600 555 318</li>
    <li><svg viewBox="0 0 12 12"><rect x="1" y="2.5" width="10" height="7" fill="none" stroke="var(--brand-red)" stroke-width="1.3"/><path d="M1 2.5 L6 6.5 L11 2.5" fill="none" stroke="var(--brand-red)" stroke-width="1.3"/></svg>lferrandis@telvano.es</li>
    <li><svg viewBox="0 0 12 12"><circle cx="6" cy="6" r="4.8" fill="none" stroke="var(--brand-red)" stroke-width="1.3"/><path d="M1.2 6 H10.8 M6 1.2 C3.5 4 3.5 8 6 10.8 M6 1.2 C8.5 4 8.5 8 6 10.8" fill="none" stroke="var(--brand-red)" stroke-width="1"/></svg>www.telvano.es</li>
    <li><svg viewBox="0 0 12 12"><circle cx="6" cy="6" r="5" fill="var(--brand-red)"/></svg>luciaferrandis</li>
  </ul>
</section>

</body>
</html>
```